Online Greeting Card Marketplace redesign

QuillPostly.com is a two-sided greeting card marketplace. Buyers purchase hand-made cards online, indicating their message. Sellers hand-write the message and mail directly to recipient.

We are getting decent foot traffic but low sales. I'm also not drawing a lot of Card Designers to sell their products. Feedback has been that it's cluttered, boring, and out of date.

I've always enjoyed vibes such as Dana Whitlock and Rosalind Perry. I was going for pale blues and chocolate browns (as can be seen in QuillPostly Facebook and Twitter pages).

Attached document is my not-so-great attempt to redesign, which is uninviting and unpolished.

Need a new homepage and a second similar page when shopping (click on any category to see what I mean, e.g. Halloween).

Industry/Entity Type

Shopping

Requirements
Must have
• I think my logo (stick drawing of a man with an envelope) is what is currently driving a lot of traffic and should stay in the design, pending minor tweaks.

I'll need all the details of the final design to give to the programmers (font styles, color numbers, etc).

Nice to have
• I was thinking of a dotted frame to surround each picture? Frost Glimmer luminescent or a metallic? I just don't know if it works.

```html
<!DOCTYPE html>
<html lang="en">
<head>
<meta charset="utf-8">
<title>QuillPostly.com — Handmade Greeting Cards</title>
<link href="https://fonts.googleapis.com/css2?family=Lato:wght@400;700&family=Damion&display=swap" rel="stylesheet">
<style>
  :root {
    --teal: #5db8c8;
    --teal-dark: #4aa5b6;
    --sky: #d3eff6;
    --sky-stripe: #c6e8f1;
    --coral: #f47a7a;
    --periwinkle: #6d84c2;
    --nav-teal: #4fb0c2;
    --nav-purple: #5b63a6;
    --nav-orange: #f08a24;
    --link-yellow: #f4e86a;
    --paper: #f5f5f3;
    --paper-line: #ecece9;
    --ink: #3a2b26;
    --muted: #8a8582;
    --white: #ffffff;
  }
  * { box-sizing: border-box; margin: 0; padding: 0; }
  html, body { width: 1087px; height: 1200px; overflow: hidden; }
  body {
    font-family: "Lato", sans-serif;
    color: var(--ink);
    background: var(--paper);
  }
  .page {
    position: relative;
    width: 1087px;
    height: 1200px;
    overflow: hidden;
    background:
      repeating-linear-gradient(180deg, transparent 0 17px, var(--paper-line) 17px 18px),
      var(--paper);
  }

  /* top bar */
  .topbar {
    position: absolute; left: 0; top: 0; width: 100%; height: 42px;
    background: var(--teal);
    z-index: 2;
  }
  .topbar::after {
    content: ""; position: absolute; left: 0; top: 42px; width: 100%; height: 8px;
    background: radial-gradient(circle at 7px 0, var(--teal) 6.5px, transparent 7px) repeat-x;
    background-size: 14px 8px;
  }
  .welcome {
    position: absolute; left: 143px; top: 15px;
    font-size: 11.5px; color: var(--white);
  }
  .welcome a { color: var(--link-yellow); text-decoration: none; }
  .search {
    position: absolute; left: 526px; top: 10px; width: 285px; height: 22px;
    background: #eef9fb; border-radius: 3px;
    font-size: 9.5px; color: #7aa8b2; letter-spacing: .5px;
    padding: 5px 10px;
  }
  .search svg { position: absolute; right: 7px; top: 4px; }
  .cart-icon { position: absolute; left: 866px; top: 10px; }
  .cart-label {
    position: absolute; left: 906px; top: 7px;
    font-size: 9px; font-weight: 700; color: var(--white); letter-spacing: .3px;
  }
  .cart-count {
    position: absolute; left: 905px; top: 20px; width: 31px; height: 13px;
    background: #f0486e; border-radius: 2px;
    font-size: 9px; font-weight: 700; color: var(--white); text-align: center; line-height: 13px;
  }

  /* hero */
  .hero {
    position: absolute; left: 0; top: 42px; width: 100%; height: 323px;
    background: repeating-linear-gradient(90deg, var(--sky) 0 3px, var(--sky-stripe) 3px 5px);
    overflow: hidden;
  }
  .hero-cards {
    position: absolute; left: 190px; bottom: 0; width: 757px; height: 55px;
    background: linear-gradient(180deg, #dcf3f8, #d4eff5);
  }
  .brand {
    position: absolute; left: 143px; top: 95px;
    display: flex; align-items: center; gap: 8px;
    font-size: 25px; font-weight: 700; color: var(--ink);
  }
  .brand-dot { width: 20px; height: 20px; border-radius: 50%; background: var(--teal); }
  .main-nav {
    position: absolute; top: 80px; right: 143px;
    display: flex; gap: 20px; align-items: center;
    font-size: 11px; letter-spacing: .1px;
  }
  .main-nav a { text-decoration: none; }
  .nav-holidays {
    color: var(--coral); border: 1px dashed #b59b9b; padding: 4px 6px; background: #f3fbfd;
  }
  .nav-everyday { color: var(--nav-teal); }
  .nav-birthdays { color: var(--nav-purple); }
  .nav-all { color: var(--nav-orange); }
  .tagline {
    position: absolute; left: 0; top: 140px; width: 100%; text-align: center;
    font-family: "Damion", cursive; font-size: 44px; font-weight: 400; color: var(--white);
    text-shadow: 0 1px 2px rgba(80,140,160,.35);
    line-height: 1.1;
  }
  .steps-line {
    position: absolute; left: 212px; top: 232px; width: 668px;
    border-top: 1px dashed var(--white);
  }
  .step-num {
    position: absolute; top: 216px; width: 32px; height: 32px; border-radius: 50%;
    border: 3px solid var(--white); color: var(--white);
    font-size: 12px; font-weight: 700; text-align: center; line-height: 26px;
  }
  .step-btn {
    position: absolute; top: 264px; width: 190px; height: 33px;
    color: var(--white); font-size: 12.5px; text-align: center; line-height: 33px;
    border-radius: 2px; box-shadow: 0 2px 0 rgba(0,0,0,.08);
  }
  .is-coral { background: var(--coral); }
  .is-teal { background: var(--teal); }
  .is-blue { background: var(--periwinkle); }

  /* sections */
  .section-head {
    position: absolute; left: 143px; width: 807px; display: flex; align-items: center;
  }
  .section-title {
    font-family: "Damion", cursive; font-size: 34px; font-weight: 400; color: var(--ink); white-space: nowrap;
  }
  .section-rule { flex: 1; border-top: 1px dashed #8a8582; margin: 6px 14px 0; }
  .see-all {
    width: 75px; height: 30px; background: var(--teal); color: var(--white);
    font-size: 12.5px; font-weight: 700; text-align: center; line-height: 30px;
    border-radius: 2px; box-shadow: 0 2px 0 var(--teal-dark);
  }
  .card { position: absolute; width: 191px; }
  .card-frame {
    height: 197px; border: 2px dotted #3a2b26; padding: 6px; background: var(--white);
  }
  .card-art { width: 100%; height: 100%; }
  .card-title { margin-top: 9px; font-size: 16.5px; font-weight: 700; }
  .card-by { font-size: 10.5px; color: var(--muted); margin-top: 1px; }

  .art-bats { background: linear-gradient(180deg, #4a4a4a, #2c2c2c); }
  .art-wolf { background: linear-gradient(180deg, #1c1c1c, #050505); }
  .art-ship { background: linear-gradient(180deg, #d8e0e7, #2e3b58); }
  .art-horse { background: linear-gradient(180deg, #e6e6e6, #5a5a5a); }
  .art-whale { background: linear-gradient(180deg, #f6f4f6, #d6cbd5); }
  .art-hive { background: linear-gradient(180deg, #3c3c3c, #242424); }
  .art-flowers { background: linear-gradient(180deg, #f4f7fa, #e2ecee); }
  .art-bird { background: linear-gradient(180deg, #f8f1ab, #eee496); }

  /* footer */
  .footer {
    position: absolute; left: 0; top: 1140px; width: 100%; height: 60px; background: var(--teal);
  }
  .footer::before {
    content: ""; position: absolute; left: 0; top: -8px; width: 100%; height: 8px;
    background: radial-gradient(circle at 7px 8px, var(--teal) 6.5px, transparent 7px) repeat-x;
    background-size: 14px 8px;
  }
  .copyright { position: absolute; left: 143px; top: 24px; font-size: 9.5px; color: var(--white); }
  .footer-nav {
    position: absolute; right: 143px; top: 16px; display: flex; gap: 20px; align-items: center;
    font-size: 9.5px; color: var(--white);
  }
  .social-dot { width: 17px; height: 17px; border-radius: 50%; background: var(--white); opacity: .9; }
</style>
</head>
<body>
<div class="page">

  <section class="hero">
    <div class="hero-cards" role="img" aria-label="Row of pale outlined greeting cards along the bottom of the banner"></div>
  </section>

  <header class="topbar">
    <p class="welcome">Welcome Visitor you can <a href="#">Sign In</a> or <a href="#">create an account</a></p>
    <div class="search">SEARCH
      <svg width="14" height="14" viewBox="0 0 14 14"><circle cx="8" cy="6" r="4.2" fill="none" stroke="#7aa8b2" stroke-width="1.4"/><line x1="5" y1="9" x2="1.5" y2="12.5" stroke="#7aa8b2" stroke-width="1.6"/></svg>
    </div>
    <svg class="cart-icon" width="26" height="22" viewBox="0 0 26 22">
      <path d="M8 9 L13 2 L18 9" fill="none" stroke="#fff" stroke-width="2.2"/>
      <path d="M2 8 H24 L21 20 H5 Z" fill="none" stroke="#fff" stroke-width="2.4" stroke-linejoin="round"/>
    </svg>
    <span class="cart-label">CART</span>
    <span class="cart-count">2</span>
  </header>

  <div class="brand"><span class="brand-dot"></span>QuillPostly.com</div>

  <nav class="main-nav">
    <a class="nav-holidays" href="#">UPCOMING HOLIDAYS</a>
    <a class="nav-everyday" href="#">EVERY DAY CARDS</a>
    <a class="nav-birthdays" href="#">BIRTHDAYS</a>
    <a class="nav-all" href="#">ALL CATEGORIES</a>
  </nav>

  <h1 class="tagline">hand made, hand written, hand delivered</h1>

  <div class="steps-line"></div>
  <span class="step-num is-coral" style="left:286px">1</span>
  <span class="step-num is-teal" style="left:531px">2</span>
  <span class="step-num is-blue" style="left:767px">3</span>
  <a class="step-btn is-coral" style="left:211px">CHOOSE A CARD</a>
  <a class="step-btn is-teal" style="left:448px">CUSTOMIZE IT</a>
  <a class="step-btn is-blue" style="left:688px">WE HANDWRITE AND MAIL</a>

  <div class="section-head" style="top:406px">
    <h2 class="section-title">Upcoming Holidays</h2>
    <span class="section-rule"></span>
    <a class="see-all">See All</a>
  </div>

  <article class="card" style="left:142px;top:464px">
    <div class="card-frame"><div class="card-art art-bats" role="img" aria-label="Paper-cut bats flying across a pale moon"></div></div>
    <h3 class="card-title">Halloween</h3><p class="card-by">By Creator</p>
  </article>
  <article class="card" style="left:347px;top:464px">
    <div class="card-frame"><div class="card-art art-wolf" role="img" aria-label="White paper-cut wolf howling at a crescent moon on black"></div></div>
    <h3 class="card-title">Halloween</h3><p class="card-by">By Creator</p>
  </article>
  <article class="card" style="left:551px;top:464px">
    <div class="card-frame"><div class="card-art art-ship" role="img" aria-label="Paper-cut sailing ship on a navy sea"></div></div>
    <h3 class="card-title">Labor Day</h3><p class="card-by">By Creator</p>
  </article>
  <article class="card" style="left:755px;top:464px">
    <div class="card-frame"><div class="card-art art-horse" role="img" aria-label="Black paper-cut horse on white"></div></div>
    <h3 class="card-title">Labor Day</h3><p class="card-by">By Creator</p>
  </article>

  <div class="section-head" style="top:741px">
    <h2 class="section-title">New Cards</h2>
    <span class="section-rule"></span>
    <a class="see-all">See All</a>
  </div>

  <article class="card" style="left:142px;top:801px">
    <div class="card-frame"><div class="card-art art-whale" role="img" aria-label="Watercolour whale illustration among seaweed"></div></div>
    <h3 class="card-title">Birthday</h3><p class="card-by">By Creator</p>
  </article>
  <article class="card" style="left:347px;top:801px">
    <div class="card-frame"><div class="card-art art-hive" role="img" aria-label="Chalkboard illustration of a beehive with a sweet message"></div></div>
    <h3 class="card-title">Anniversary</h3><p class="card-by">By Creator</p>
  </article>
  <article class="card" style="left:551px;top:801px">
    <div class="card-frame"><div class="card-art art-flowers" role="img" aria-label="Quilled paper flowers on white"></div></div>
    <h3 class="card-title">Bereavement</h3><p class="card-by">By Creator</p>
  </article>
  <article class="card" style="left:755px;top:801px">
    <div class="card-frame"><div class="card-art art-bird" role="img" aria-label="Drawn bluebird on a flowering branch over pale yellow"></div></div>
    <h3 class="card-title">New Baby</h3><p class="card-by">By Creator</p>
  </article>

  <footer class="footer">
    <p class="copyright">All rights reserved © 2011-2013 QuillPostly</p>
    <nav class="footer-nav">
      <span>About Us/FAQ</span><span>Contact</span><span>Follow Us</span>
      <span class="social-dot" role="img" aria-label="Social profile link"></span>
      <span class="social-dot" role="img" aria-label="Social profile link"></span>
    </nav>
  </footer>

</div>
</body>
</html>
```